Floristry Business Card Design Project

I have a logo now and am looking to incorporate this into a business card. I would like a double sided business card. I would like one side to be decorative so that it blends well when included with floral arrangements and that can also be used as the front of a card and the other side will contain the business details. The font on the business details side should be clear although some decorative font would be ok. I have included the logo files for use in the business card design.

Feel free to break up the logo and use certain aspects of it in the design. Really looking for something that stands out and that is really creative.

Industry/Entity Type

Floral

Requirements
Should not have
• Nothing tacky or corny. The logo should be clearly read (perhaps a background colour).

```html
<!DOCTYPE html>
<html lang="en">
<head>
<meta charset="utf-8">
<title>Petal Hollow – Business Card</title>
<link rel="stylesheet" href="https://fonts.googleapis.com/css2?family=Cinzel:wght@400&family=Cormorant+Garamond:wght@500&display=swap">
<style>
  :root {
    --backdrop: #58585a;
    --label: #a9a9ab;
    --paper: #f3f2ef;
    --salmon: #e0896a;
    --green: #55a776;
    --lime: #98bd45;
    --sea: #6cbf9f;
  }
  * { margin: 0; padding: 0; box-sizing: border-box; }
  html, body { width: 1200px; height: 900px; overflow: hidden; }
  body {
    background: var(--backdrop);
    position: relative;
    font-family: "Cinzel", serif;
  }
  .side-label {
    position: absolute;
    font-family: "Cormorant Garamond", serif;
    font-size: 12px;
    letter-spacing: 1.5px;
    color: var(--label);
  }
  .side-label--back { left: 235px; top: 278px; }
  .side-label--front { left: 235px; top: 603px; }

  .card {
    position: absolute;
    left: 330px;
    width: 540px;
    height: 275px;
    background: var(--paper);
    box-shadow: 0 2px 6px rgba(0,0,0,0.35);
  }
  .card--back { top: 150px; }
  .card--front { top: 475px; overflow: hidden; }

  .brand-mark {
    position: absolute;
    left: 74px;
    top: 60px;
    width: 132px;
    height: 132px;
    border: 2px solid var(--green);
    border-radius: 50%;
  }
  .brand-name {
    position: absolute;
    left: 0;
    width: 280px;
    top: 203px;
    text-align: center;
    font-size: 17px;
    letter-spacing: 3px;
    color: var(--green);
  }
  .details {
    position: absolute;
    left: 296px;
    top: 66px;
  }
  .details__name {
    font-size: 20px;
    letter-spacing: 2px;
    color: var(--salmon);
  }
  .details__phone {
    margin-top: 8px;
    font-family: "Cinzel", serif;
    font-size: 13px;
    letter-spacing: 1.5px;
    color: var(--green);
  }
  .details__web {
    margin-top: 10px;
    font-family: "Cormorant Garamond", serif;
    font-size: 14px;
    letter-spacing: 2px;
    color: var(--lime);
  }
  .details__address {
    position: absolute;
    left: 296px;
    top: 190px;
    font-size: 11px;
    line-height: 17px;
    letter-spacing: 1px;
    color: var(--salmon);
  }
  .floral-pattern {
    width: 100%;
    height: 100%;
    background:
      radial-gradient(circle at 18% 28%, rgba(224,137,106,0.55) 0, rgba(224,137,106,0) 22%),
      radial-gradient(circle at 62% 22%, rgba(224,137,106,0.45) 0, rgba(224,137,106,0) 20%),
      radial-gradient(circle at 40% 75%, rgba(224,137,106,0.5) 0, rgba(224,137,106,0) 22%),
      radial-gradient(circle at 84% 40%, rgba(108,191,159,0.5) 0, rgba(108,191,159,0) 22%),
      radial-gradient(circle at 10% 82%, rgba(152,189,69,0.45) 0, rgba(152,189,69,0) 20%),
      radial-gradient(circle at 70% 80%, rgba(152,189,69,0.45) 0, rgba(152,189,69,0) 20%),
      radial-gradient(circle at 30% 50%, rgba(108,191,159,0.35) 0, rgba(108,191,159,0) 18%),
      var(--paper);
  }
</style>
</head>
<body>
  <span class="side-label side-label--back">BACK</span>
  <span class="side-label side-label--front">FRONT</span>

  <section class="card card--back">
    <div class="brand-mark" aria-hidden="true"></div>
    <p class="brand-name">Petal Hollow</p>
    <div class="details">
      <p class="details__name">Your Name</p>
      <p class="details__phone">+91 9000123456</p>
      <p class="details__web">petalhollow.com</p>
    </div>
    <p class="details__address">7-LGF, Maple Heights<br>Street Xyz, Country</p>
  </section>

  <section class="card card--front">
    <div class="floral-pattern" role="img" aria-label="Scattered hand-drawn floral pattern of salmon poppies, green leaves, teal sprigs and lime fronds on off-white paper"></div>
  </section>
</body>
</html>
```